Box design for toddler shoes

Hi,

TASK:
I need a shoe box designed for our rubber soled socks.

DIMENSION:
13.5cmHx12cmWx7.2cmD

​BOX FEATURE:
1. Must include the following information
a) our logo
b) the product name ‘Rubber Soled Socks’
c) Some product key features that could be written on the box include:
- Indoor and outdoor wear
- Soft and flexible sole
- Light weight and comfortable
d) Sock composition and care instructions also needs to be included on the box,
probably quite small. Maybe on the base.

Sock: 80% Cotton 10% Spandex 10% Polyester
Rubber Sole

Care instructions:
Cold Machine Wash or Hand Wash
Do not bleach
Do not tumble dry

Made in China
Distributed by LW Tots
www.lwtots-sample.com.au

2. A CUT OUT in the lid so you can see at least part of the shoe/sock pattern design. I am open to different size and shape cut outs, but need the shoes to not be at risk of falling out of the box.

DESIGN KEYPOINTS:
1. I would like a modern classic design. I like the yellow shoe box picture attached, but am happy and open for a different design. This just gives you the idea of the fresh look I like.

2. NO brown craft packaging, but am open to options for other colours.

3. NO picture of the socks on the box design
- the CUT on the lid will allow buyer to see the pattern on the socks. Attached is images of the sample shoe/socks that will be put in the boxes and how they will be packaged in the rectangle box. There are many different designs/colour. All will need to be packaged in the same box.

4. I'd love to see what the box would look like as it sits on the shelf, but also need the flat lay design ready for printing.

Please let me know if you have any questions to help with your design.

I can't wait to see your design.

Thanks,
Maren

Industry/Entity Type

Baby/kids

Font styles to use
Sans Serif
Other font styles liked:
• More modern version of Sans Serif

Requirements
Must have
• Cut out in the top of the box so you can see part of the sock to know which design is packaged inside.
Should not have
• Bubble font

```html
<!DOCTYPE html>
<html lang="en">
<head>
<meta charset="utf-8">
<title>Little Wren Rubber Soled Socks – Box Dielines</title>
<link href="https://fonts.googleapis.com/css2?family=Poppins:wght@600;700&family=Zilla+Slab:wght@400&family=Nunito:wght@400&display=swap" rel="stylesheet">
<style>
  :root {
    --bg: #fff8c0;
    --yellow: #ffcc0a;
    --lemon: #fff200;
    --white: #ffffff;
    --pink: #e4007c;
    --ink: #333333;
    --guide: #29abe2;
    --window-text: #c8c8c8;
  }
  html, body { margin: 0; padding: 0; overflow: hidden; background: var(--bg); }
  .canvas { position: relative; width: 1200px; height: 1006px; overflow: hidden; background: var(--bg); }
  .dielines { position: absolute; inset: 0; width: 1200px; height: 1006px; }
  .guide { fill: none; stroke: var(--guide); stroke-width: 0.8; }
  .panel-yellow { fill: var(--yellow); }
  .swoosh-lemon { fill: var(--lemon); }
  .swoosh-white { fill: var(--white); }
  .notch { fill: var(--white); opacity: .8; }
  .brand-name { font-family: "Poppins", sans-serif; font-weight: 600; fill: var(--pink); }
  .product-name { font-family: "Poppins", sans-serif; font-weight: 700; fill: var(--pink); }
  .feature { font-family: "Zilla Slab", serif; fill: var(--pink); }
  .care-head { font-family: "Nunito", sans-serif; font-size: 7px; fill: var(--ink); text-anchor: middle; }
  .care-line { font-family: "Nunito", sans-serif; font-size: 7px; fill: var(--pink); text-anchor: middle; }
  .window-label { font-family: "Zilla Slab", serif; font-size: 15px; fill: var(--window-text); text-anchor: middle; }
</style>
</head>
<body>
<div class="canvas">
<svg class="dielines" viewBox="0 0 1200 1006" xmlns="http://www.w3.org/2000/svg">
  <defs>
    <linearGradient id="sockArt" x1="0" y1="0" x2="1" y2="1">
      <stop offset="0" stop-color="#ffcc0a"/>
      <stop offset="1" stop-color="#f3c6dc"/>
    </linearGradient>

    <!-- front face content -->
    <g id="face-front">
      <rect class="panel-yellow" x="347" y="111" width="270" height="271"/>
      <path class="swoosh-lemon" d="M347,212 C400,140 520,118 617,134 L617,382 L347,382 Z"/>
      <path class="swoosh-white" d="M347,222 C405,156 520,136 617,152 L617,382 L347,382 Z"/>
      <text class="brand-name" x="398" y="192" font-size="14">Little Wren</text>
      <text class="product-name" x="398" y="222" font-size="20">Rubber Soled</text>
      <text class="product-name" x="398" y="256" font-size="30">Socks</text>
      <rect x="508" y="230" width="68" height="66" rx="22" fill="url(#sockArt)" role="img" aria-label="Illustration of a rubber soled sock"/>
      <text class="feature" x="394" y="334" font-size="11.5">• Indoor and outdoor wear</text>
      <text class="feature" x="394" y="348" font-size="11.5">• Soft and flexible sole</text>
      <text class="feature" x="394" y="362" font-size="11.5">• Light weight and comfortable</text>
    </g>

    <!-- side face content -->
    <g id="face-side">
      <rect class="panel-yellow" x="24" y="371" width="333" height="171"/>
      <path class="swoosh-lemon" d="M178,371 C98,395 92,515 112,542 L357,542 L357,371 Z"/>
      <path class="swoosh-white" d="M190,371 C112,398 106,515 124,542 L357,542 L357,371 Z"/>
      <g transform="rotate(-90 205 456)">
        <text class="brand-name" x="150" y="388" font-size="9">Little Wren</text>
        <text class="product-name" x="150" y="404" font-size="12">Rubber Soled</text>
        <text class="product-name" x="150" y="425" font-size="19">Socks</text>
        <rect x="225" y="405" width="40" height="40" rx="14" fill="url(#sockArt)" role="img" aria-label="Illustration of a rubber soled sock"/>
      </g>
      <g transform="rotate(-90 320 456)">
        <text class="feature" x="260" y="430" font-size="8.5">• Indoor and outdoor wear</text>
        <text class="feature" x="260" y="441" font-size="8.5">• Soft and flexible sole</text>
        <text class="feature" x="260" y="452" font-size="8.5">• Light weight and comfortable</text>
      </g>
    </g>
  </defs>

  <!-- box body dieline -->
  <g class="box-body">
    <rect class="panel-yellow" x="347" y="49" width="270" height="816"/>
    <rect class="panel-yellow" x="24" y="371" width="916" height="171"/>
    <use href="#face-front"/>
    <use href="#face-front" transform="rotate(180 482 456.5)"/>
    <use href="#face-side"/>
    <use href="#face-side" transform="rotate(180 482 456.5)"/>

    <rect class="swoosh-white" x="357" y="382" width="250" height="149"/>
    <g class="care-info">
      <text class="care-head" x="482" y="413">Sock:</text>
      <text class="care-line" x="482" y="422">80% Cotton 10% Spandex 10% Polyester</text>
      <text class="care-line" x="482" y="431">Rubber Sole</text>
      <text class="care-head" x="482" y="448">Care instructions:</text>
      <text class="care-line" x="482" y="457">Cold Machine Wash or Hand Wash</text>
      <text class="care-line" x="482" y="466">Do not bleach</text>
      <text class="care-line" x="482" y="475">Do not tumble dry</text>
      <line x1="437" y1="479" x2="529" y2="479" stroke="var(--pink)" stroke-width=".8"/>
      <text class="care-head" x="482" y="489">Made in China</text>
      <text class="care-head" x="482" y="498">Distributed by LW Tots</text>
      <text class="care-head" x="482" y="507">www.lwtots-sample.com.au</text>
    </g>

    <rect class="notch" x="331" y="355" width="16" height="16"/>
    <rect class="notch" x="617" y="355" width="16" height="16"/>
    <rect class="notch" x="331" y="542" width="16" height="16"/>
    <rect class="notch" x="617" y="542" width="16" height="16"/>

    <rect class="guide" x="347" y="49" width="270" height="816"/>
    <rect class="guide" x="24" y="371" width="916" height="171"/>
    <rect class="guide" x="357" y="60" width="250" height="794"/>
    <rect class="guide" x="34" y="382" width="896" height="149"/>
    <line class="guide" x1="357" y1="111" x2="607" y2="111"/>
    <line class="guide" x1="357" y1="803" x2="607" y2="803"/>
    <line class="guide" x1="86" y1="382" x2="86" y2="531"/>
    <line class="guide" x1="878" y1="382" x2="878" y2="531"/>
    <line class="guide" x1="357" y1="382" x2="357" y2="531"/>
    <line class="guide" x1="607" y1="382" x2="607" y2="531"/>
  </g>

  <!-- lid dieline -->
  <g class="box-lid">
    <rect class="panel-yellow" x="737" y="17" width="429" height="339"/>
    <rect class="guide" x="831" y="17" width="242" height="339"/>
    <rect class="guide" x="737" y="110" width="429" height="153"/>
    <rect class="guide" x="839" y="27" width="224" height="320"/>
    <rect class="guide" x="747" y="120" width="410" height="134"/>
    <line class="guide" x1="839" y1="73" x2="1063" y2="73"/>
    <line class="guide" x1="839" y1="300" x2="1063" y2="300"/>
    <line class="guide" x1="793" y1="120" x2="793" y2="254"/>
    <line class="guide" x1="1110" y1="120" x2="1110" y2="254"/>
    <rect x="868" y="148" width="167" height="78" rx="39" fill="var(--white)"/>
    <text class="window-label" x="951.5" y="193">WINDOW</text>
  </g>
</svg>
</div>
</body>
</html>
```